サイト構成・基本的な要件については
https://zubalo.com/boards/kQpTrnVxaYeL42dm
を併せてご覧いただければ幸いです。

また、店舗写真・ロゴについては
http://nuvadrop.jp/get/7a1be93c50df28e47a6b0c13f8d52e9a61f7b0de
よりダウンロードいただければと存じます。

上記だけで制作が難しい場合は
http://molvu.jp/
http://jp.grenaxi.com/
http://www.plimbrook.com/ja/cat-27-Beauty-Fashion.html
などから、10000円程度までならこちらにて購入可能です。
カンプデータにて作成頂き、
納品時に当方にて購入したデータに差し替えていただければと存じます。

ページ構成もシンプルですので
TOPページからすべての導線を配置するかたちでデザインいただければと存じます。
当方、jqueryなどのコーディングも対応可能ですので、
そういったデザイン提案を頂いても大丈夫です。

色合いは、店舗に合わせた、シンプルで明るい色合いを希望いたします。
木目、ブラウンを採用しているので、
そちらを展開した形のカラーパターンが合うかなと考えていますが、
特に絶対的な指定はありません。
http://beauty.tarukami.jp/slnQ000583716/
1ページ
茶系、店舗のイメージを展開するような色合いですと幸いです。
• 高解像度JPG (.jpg)
• フォトショップ形式 (.psd)
サイト構成・基本的な要件については
を併せてご覧いただければ幸いです。

また、写真・素材については
よりダウンロードいただければと存じます。

上記だけで制作が難しい場合は
http://molvu.jp/
http://jp.grenaxi.com/
などから、10000円程度までならこちらにて購入可能です。カンプデータにて作成頂き、納品時に当方にて購入したデータに差し替えていただければと存じます。

基本的には、大きなイメージ写真を前面に出して訴求しつつ
明るいイメージでまとめられればと思います。

【参考イメージ】
http://senbarusika.jp/ (色合い、明るい印象)
http://www.mabeku.jp/home/studydesk/product/vozlan/(色合い、明るい印象)

余りかしこまった雰囲気にしてしまうよりは、柔らかく明るい印象にすることで、男女とも入りやすいサロンということをアピールできればと考えています。
制作につきましてご不明な点がございましたら、
お気軽にお申し付けいただければと存じます。
ご提案お待ちしております
ご質問にて、ワイヤーフレーム提示のご要望がありましたので追記いたします。

https://zubalo.com/boards/pHnRtc7XmW9vqdz5

上記が、当方で想定しているワイヤーですが、
あまり上記にこだわらず、ご提案頂ければ幸甚です。
ご不明な点がございましたらお気軽にお申し付けください。
http://nuvadrop.jp/get/82ce5d0a93bf714e6c2d08a1f5b937e40d6ac5b1

念のため、素材を再アップいたします。

クライアントとの協議の結果、こちらの案を採用させていただきました。
スタイリッシュなデザインとサイト全体の見やすさ、信頼感、
文字などの読みやすさが大変気に入り、
そちらが採用の決め手となりました。

この度は多数ご提案いただきありがとうございました。
当選に至らなかったランサー様におかれましては大変心苦しいのですが、
次の機会にぜひご提案いただければ幸甚です。
引き続き何卒よろしくお願いいたします。

```html
<!DOCTYPE html>
<html lang="ja">
<head>
<meta charset="utf-8">
<title>CUT STUDIO HARUNE</title>
<link rel="stylesheet" href="https://fonts.googleapis.com/css2?family=Noto+Sans+JP:wght@300;400;500&display=swap">
<style>
:root{
  --brown:#7a6352;
  --brown-dark:#5e4a3c;
  --accent:#8c6b57;
  --text:#5a5a5a;
  --muted:#888;
  --line:#dcdcdc;
  --gray-bg:#ececec;
  --nav-bg:#e9e9e9;
  --pink:#f3c8cf;
  --green:#bfe0cd;
  --white:#fff;
}
*{margin:0;padding:0;box-sizing:border-box}
html,body{width:1200px;height:3664px;overflow:hidden}
body{font-family:"Noto Sans JP",sans-serif;color:var(--text);background:var(--white);position:relative}
.abs{position:absolute}
.photo{position:absolute}

/* hero */
.hero{left:0;top:0;width:1200px;height:528px;background:linear-gradient(135deg,#d9cfc2 0%,#efe9e1 45%,#cdbfae 100%)}
.hero-logo{left:28px;top:18px;width:180px;height:180px;border-radius:50%;background:rgba(255,255,255,.92);display:flex;flex-direction:column;align-items:center;justify-content:center;color:var(--brown-dark)}
.hero-logo span{font-size:15px;letter-spacing:3px;font-weight:400}
.hero-logo strong{font-size:28px;letter-spacing:4px;font-weight:400;margin-top:4px}
.hero-catch{right:48px;top:40px;text-align:right}
.hero-catch p{display:inline-block;background:rgba(243,200,207,.9);color:var(--white);font-size:19px;letter-spacing:2px;padding:4px 14px;margin-bottom:10px}
.hero-reserve{left:780px;top:388px;width:200px;height:52px;background:var(--pink);color:var(--white);font-size:16px;display:flex;align-items:center;justify-content:center;letter-spacing:2px}

/* nav */
.gnav{left:0;top:528px;width:1200px;height:80px;background:var(--nav-bg);display:flex;justify-content:center;align-items:center}
.gnav a{display:block;width:176px;text-align:center;font-size:15px;color:var(--text);text-decoration:none;letter-spacing:1px}

/* headings */
.section-title{width:1200px;text-align:center;color:var(--accent);font-weight:400;letter-spacing:4px}

/* intro */
.intro-title{top:700px;font-size:30px}
.intro-text{top:772px;width:1200px;text-align:center;font-size:14px;line-height:26px;color:var(--muted)}

/* photo strip */
.strip-left{left:0;top:1000px;width:600px;height:320px;background:linear-gradient(90deg,#cfd9df,#f3efe8 50%,#d8cbbd)}
.strip-right{left:600px;top:1000px;width:600px;height:320px;background:linear-gradient(90deg,#eae6e0,#fbfbfa 50%,#d9d2c8)}

/* news */
.news-title{top:1408px;font-size:26px}
.news-list{left:160px;top:1510px;width:880px;list-style:none}
.news-list li{display:flex;height:64px;align-items:center;border-bottom:1px dotted var(--line);font-size:14px}
.news-list time{width:240px;color:var(--muted)}
.btn-outline{width:156px;height:36px;border:1px solid #bbb;font-size:13px;color:var(--muted);display:flex;align-items:center;justify-content:center;background:var(--white)}

/* band */
.band-sign{left:0;top:1932px;width:600px;height:308px;background:#e8e8e6;display:flex;flex-direction:column;justify-content:center;padding-left:110px;color:#444}
.band-sign span{font-size:30px;letter-spacing:6px}
.band-sign strong{font-size:70px;font-weight:400;letter-spacing:8px;line-height:1.1}
.band-photo{left:600px;top:1932px;width:600px;height:308px;background:linear-gradient(90deg,#8a6a4e,#d8c9b2 50%,#6c4e37)}

/* gallery */
.gallery-title{top:2352px;font-size:26px}
.gal{top:2460px;width:240px;height:260px;background:linear-gradient(180deg,#e9eef0,#c8b7a5)}

/* access */
.access-info{left:0;top:2912px;width:600px;height:428px;background:var(--gray-bg);padding:48px 0 0 116px;color:#444}
.access-logo span{font-size:16px;letter-spacing:3px}
.access-logo strong{display:block;font-size:40px;font-weight:400;letter-spacing:6px;line-height:1.1}
.access-tel{font-size:20px;margin-top:26px;letter-spacing:1px}
.access-detail{font-size:13px;line-height:22px;margin-top:8px;color:var(--text)}
.access-btns{display:flex;gap:20px;margin-top:60px}
.access-btns span{width:150px;height:44px;display:flex;align-items:center;justify-content:center;color:var(--white);font-size:14px}
.access-btns .reserve{background:var(--green);color:#4d6d5b}
.access-btns .recruit{background:var(--pink)}
.map{left:600px;top:2912px;width:600px;height:428px;background:linear-gradient(135deg,#e6e2d8,#f3f0ea 50%,#ddd8cc)}

/* footer */
.footer{left:0;top:3340px;width:1200px;height:324px;background:var(--brown);color:var(--white)}
.fnav{position:absolute;left:0;width:1200px;display:flex;justify-content:center}
.fnav a{color:var(--white);text-decoration:none;font-size:13px;padding:0 34px;border-right:1px solid rgba(255,255,255,.4)}
.fnav a:first-child{border-left:1px solid rgba(255,255,255,.4)}
.fnav-1{top:140px}
.fnav-2{top:192px}
.copyright{position:absolute;top:276px;width:1200px;text-align:center;font-size:11px;color:rgba(255,255,255,.8)}
.pagetop{position:absolute;right:30px;top:264px}
</style>
</head>
<body>

<section class="abs hero" role="img" aria-label="サロン店内のシャンプー台とセット面の写真">
</section>
<div class="abs hero-logo"><span>CUT STUDIO</span><strong>HARUNE</strong></div>
<div class="abs hero-catch">
  <p>美容師になって良かったと思われる</p><br>
  <p>すべてのお客様のためのヘアサロンです</p>
</div>
<a class="abs hero-reserve">ご予約はこちら</a>

<nav class="abs gnav">
  <a>サロン案内</a><a>メニュー・料金</a><a>シャンプーについて</a><a>スタッフ紹介</a><a>よくある質問</a><a>ギャラリー</a>
</nav>

<h2 class="abs section-title intro-title">スタイリスト全員が理容・美容両方の免許保持者</h2>
<p class="abs intro-text">
  当店は男女問わず気軽に通っていただけるヘアサロンです。<br>
  カットからカラーまで丁寧な技術でお応えいたします。<br>
  落ち着いた空間でゆったりとお過ごしください。<br>
  スタッフ一同、皆様のご来店を心よりお待ちしております。<br>
  理容・美容の両方の資格を活かしたご提案をいたします。<br>
  ご予約はお電話またはWebより承っております。
</p>

<div class="photo strip-left" role="img" aria-label="ヘアケア製品のボトルが並ぶ写真"></div>
<div class="photo strip-right" role="img" aria-label="白いシャンプー台が並ぶ店内の写真"></div>

<h2 class="abs section-title news-title">新着情報</h2>
<ul class="abs news-list">
  <li><time>2000.00.00</time>ここに新着情報が入ります。ここに新着情報が入ります。ここに新着情報が入ります。</li>
  <li><time>2000.00.00</time>ここに新着情報が入ります。ここに新着情報が入ります。ここに新着情報が入ります。</li>
  <li><time>2000.00.00</time>ここに新着情報が入ります。ここに新着情報が入ります。ここに新着情報が入ります。</li>
  <li><time>2000.00.00</time>ここに新着情報が入ります。ここに新着情報が入ります。ここに新着情報が入ります。</li>
</ul>
<a class="abs btn-outline" style="left:892px;top:1800px">一覧を見る</a>

<div class="abs band-sign"><span>CUT STUDIO</span><strong>HARUNE</strong></div>
<div class="photo band-photo" role="img" aria-label="木目の受付カウンターがある店内の写真"></div>

<h2 class="abs section-title gallery-title">ギャラリー</h2>
<div class="photo gal" style="left:160px" role="img" aria-label="ロングヘアのスタイル写真"></div>
<div class="photo gal" style="left:480px" role="img" aria-label="メンズショートのスタイル写真"></div>
<div class="photo gal" style="left:800px" role="img" aria-label="ロングヘアのスタイル写真"></div>
<a class="abs btn-outline" style="left:892px;top:2772px">もっと見る</a>

<section class="abs access-info">
  <div class="access-logo"><span>CUT STUDIO</span><strong>HARUNE</strong></div>
  <p class="access-tel">TEL 045-762-3190</p>
  <p class="access-detail">
    平日 9:00〜20:00 / 土日祝 9:00〜19:00<br>
    神奈川県横浜市緑葉区若草町123-45<br>
    若草駅より徒歩7分
  </p>
  <div class="access-btns"><span class="reserve">ご予約はこちら</span><span class="recruit">採用情報</span></div>
</section>
<div class="photo map" role="img" aria-label="サロン周辺の地図"></div>

<footer class="abs footer">
  <div class="fnav fnav-1"><a>サロン案内</a><a>メニュー・料金</a><a>シャンプーについて</a><a>スタッフ紹介</a><a>よくある質問</a><a>ギャラリー</a></div>
  <div class="fnav fnav-2"><a>HOME</a><a>プライバシーポリシー</a><a>サイトマップ</a></div>
  <p class="copyright">Copyright © Harune All Rights Reserved.</p>
  <svg class="pagetop" width="40" height="28" viewBox="0 0 40 28"><polyline points="4,24 20,6 36,24" fill="none" stroke="#fff" stroke-width="3"/></svg>
</footer>

</body>
</html>
```